Business card design needed

We need a new business card design to re launch my carpentry business. Could include double sided card with list of services provided.
Kitchens, bathrooms, decks, pergolas, window replacements, timber floor installation, owner builder assistance and general carpentry.
Would like an eye catching card that becons to be read in bright colors that has a logo that could be also used on clothing vehicle sinage etc
Preferably in blues and reds we live near beach so maybe some type of Beecher feel
Target Market(s)
The target market of my business would be mainly individuals requiring professional carpentry services not just a handy man. The renovation market plays a big part of my business
Industry/Entity Type
Carpentry
Contact Information for Business Card
Carpenter & joiner
Rob Pelham
Inverloch
gilda_robbo@tarnmail.com
0439862150
Look and feel
Each slider illustrates characteristics of the customer's brand and the style your logo design should communicate.

```html
<!DOCTYPE html>
<html lang="en">
<head>
<meta charset="utf-8">
<title>Rob Pelham – Carpenter &amp; Joiner business card</title>
<link rel="stylesheet" href="https://fonts.googleapis.com/css2?family=Nunito:wght@400;700;800;900&family=Varela+Round&display=swap">
<style>
  :root {
    --stage: #000000;
    --coral: #c94545;
    --coral-soft: #e89a98;
    --ocean: #2fc4d8;
    --sand: #f0934e;
    --ink: #3a1212;
    --paper: #ffffff;
  }
  html, body {
    margin: 0;
    width: 1200px;
    height: 1000px;
    overflow: hidden;
    background: var(--stage);
  }
  .canvas {
    position: relative;
    width: 1200px;
    height: 1000px;
  }
  .card {
    position: absolute;
    top: 96px;
    width: 457px;
    height: 790px;
    box-sizing: border-box;
  }
  .card--front {
    left: 88px;
    background: var(--coral);
  }
  .card--back {
    left: 659px;
    background: var(--paper);
    border: 1px solid var(--coral);
  }
  .centered {
    position: absolute;
    left: 0;
    width: 100%;
    text-align: center;
  }

  /* front */
  .front-glow {
    position: absolute;
    left: 58px;
    top: 140px;
    width: 340px;
    height: 340px;
    border-radius: 50%;
    background: radial-gradient(circle, var(--ocean) 0%, var(--ocean) 48%, rgba(47,196,216,0.35) 62%, rgba(201,69,69,0) 72%);
  }
  .brand-mark {
    top: 262px;
    font-family: "Nunito", sans-serif;
    font-weight: 900;
    font-size: 40px;
    color: var(--sand);
    letter-spacing: 0.5px;
  }
  .owner-first {
    top: 392px;
    font-family: "Nunito", sans-serif;
    font-weight: 800;
    font-size: 30px;
    color: var(--paper);
  }
  .owner-last {
    top: 424px;
    font-family: "Nunito", sans-serif;
    font-weight: 900;
    font-size: 45px;
    color: var(--paper);
    letter-spacing: 0.5px;
  }
  .trade-rule {
    position: absolute;
    top: 538px;
    width: 3px;
    height: 76px;
    background: var(--paper);
    border-radius: 2px;
  }
  .trade-rule--left { left: 86px; }
  .trade-rule--right { left: 364px; }
  .trade {
    top: 552px;
    font-family: "Varela Round", sans-serif;
    font-size: 24px;
    color: var(--ink);
  }
  .location {
    top: 584px;
    font-family: "Varela Round", sans-serif;
    font-size: 17px;
    letter-spacing: 6px;
    color: var(--paper);
  }

  /* back */
  .services {
    top: 120px;
    margin: 0;
    padding: 0;
    list-style: none;
    font-family: "Varela Round", sans-serif;
    font-size: 29px;
    line-height: 39px;
  }
  .services li:nth-child(odd) { color: var(--coral); }
  .services li:nth-child(even) { color: var(--coral-soft); }
  .back-mark {
    top: 504px;
    font-family: "Nunito", sans-serif;
    font-weight: 900;
    font-size: 34px;
    color: var(--coral);
  }
  .back-name {
    top: 590px;
    font-family: "Nunito", sans-serif;
    font-weight: 800;
    font-size: 26px;
    color: var(--coral);
  }
  .back-email {
    top: 636px;
    font-family: "Varela Round", sans-serif;
    font-size: 24px;
    color: var(--ink);
  }
  .back-phone {
    top: 668px;
    font-family: "Varela Round", sans-serif;
    font-size: 26px;
    color: var(--ink);
  }
</style>
</head>
<body>
<main class="canvas">
  <section class="card card--front" aria-label="Card front">
    <div class="front-glow"></div>
    <div class="centered brand-mark">Rob Pelham</div>
    <div class="centered owner-first">Rob</div>
    <div class="centered owner-last">PELHAM</div>
    <span class="trade-rule trade-rule--left"></span>
    <span class="trade-rule trade-rule--right"></span>
    <div class="centered trade">Carpenter &amp; Joiner</div>
    <div class="centered location">INVERLOCH</div>
  </section>

  <section class="card card--back" aria-label="Card back">
    <ul class="centered services">
      <li>kitchens</li>
      <li>bathrooms</li>
      <li>decks</li>
      <li>pergolas</li>
      <li>window replacements</li>
      <li>timber floor installation</li>
      <li>owner builder assistance</li>
      <li>general carpentry</li>
    </ul>
    <div class="centered back-mark">Rob Pelham</div>
    <div class="centered back-name">Rob Pelham</div>
    <div class="centered back-email">gilda_robbo@tarnmail.com</div>
    <div class="centered back-phone">Tel: 0439862150</div>
  </section>
</main>
</body>
</html>
```